Studying Effectively To Do List

I am looking to design a new "Study To Do List" for High School students (Ages 15 - 18) . This will be printed as an A4 notepad and so should only be a single A4 page.

The Design will need to be professional and look semi-serious but also be appealing to High school students (Ages 15 - 18) and should NOT be gender specific.

I have attached a word document outlining the structure of the page. The space provided should be large enough that people can write in it comfortably.

The notepad will most likely be printed in black and white but I'm also looking at coloured options - colours should be kept to a minimum.

This will be printed professionally and should also include a 3mm bleed.

The design should also include the business logo (included in the word document)

Target Market(s)

High School students (Ages 15 - 18). Both genders

Industry/Entity Type

Education

Font styles to use
Serif
Sans Serif

Requirements
Must have
• Please see the word document attached.
Should not have
• Too much colour

```html
<!DOCTYPE html>
<html lang="en">
<head>
<meta charset="utf-8">
<title>Study To Do List</title>
<link href="https://fonts.googleapis.com/css2?family=Montserrat:wght@400;500;800&display=swap" rel="stylesheet">
<style>
  :root {
    --backdrop: #b9c8d6;
    --paper: #f3f4f6;
    --panel: #f8f9fb;
    --navy: #2e475e;
    --ink: #1f3247;
    --rule: #9aa3ad;
    --accent: #e8833a;
  }
  * { box-sizing: border-box; margin: 0; padding: 0; }
  html, body { width: 1200px; height: 1200px; overflow: hidden; }
  body {
    background: var(--backdrop);
    font-family: "Montserrat", sans-serif;
    color: var(--ink);
  }
  .sheet {
    position: absolute;
    left: 204px; top: 30px;
    width: 792px; height: 1140px;
    padding: 22px 26px 24px;
    background: linear-gradient(to bottom, var(--paper) 0%, var(--paper) 24%, var(--navy) 58%, var(--navy) 100%);
    display: flex; flex-direction: column; gap: 12px;
  }
  .masthead {
    height: 78px;
    display: flex; align-items: center; justify-content: space-between;
  }
  .brand { display: flex; align-items: center; gap: 10px; }
  .brand-dot { width: 22px; height: 22px; border-radius: 50%; background: var(--accent); }
  .brand-name { font-weight: 800; font-size: 20px; color: var(--ink); letter-spacing: .5px; }
  .date-field { display: flex; align-items: flex-end; gap: 10px; font-weight: 800; font-size: 18px; }
  .date-field span.line { width: 200px; border-bottom: 1px solid var(--rule); height: 18px; }
  .panel {
    background: var(--panel);
    border-radius: 14px;
    padding: 12px 18px 14px;
  }
  .panel-title { font-weight: 800; font-size: 17px; letter-spacing: .3px; margin-bottom: 6px; }
  .revision { border: 1px solid var(--accent); }
  .revision-cols { display: grid; grid-template-columns: 1fr 1fr; gap: 30px; }
  .row {
    display: flex; align-items: flex-end; gap: 8px;
    height: 24px; font-size: 11px; font-weight: 500;
  }
  .row .line { flex: 1; border-bottom: 1px solid var(--rule); height: 100%; }
  .row .label { width: 70px; }
  .row .num { width: 16px; }
  .row .due { margin-left: 14px; }
  .row .due-line { flex: 0 0 120px; border-bottom: 1px solid var(--rule); height: 100%; }
  .bottom-row { display: grid; grid-template-columns: 1fr 1fr; gap: 0; flex: 1; }
  .bottom-row .panel { border-radius: 14px; }
  .notes { border-right: 1px solid var(--accent); border-radius: 14px 0 0 14px !important; }
  .practice { border-radius: 0 14px 14px 0 !important; }
</style>
</head>
<body>
<main class="sheet">
  <header class="masthead">
    <div class="brand"><span class="brand-dot"></span><span class="brand-name">Kestrel Study</span></div>
    <div class="date-field">DATE:<span class="line"></span></div>
  </header>

  <section class="panel revision">
    <h2 class="panel-title">REVISION</h2>
    <div class="revision-cols">
      <div>
        <div class="row"><span class="num">1.</span><span class="line"></span></div>
        <div class="row"><span class="num">2.</span><span class="line"></span></div>
        <div class="row"><span class="num">3.</span><span class="line"></span></div>
        <div class="row"><span class="num">4.</span><span class="line"></span></div>
      </div>
      <div>
        <div class="row"><span class="num">5.</span><span class="line"></span></div>
        <div class="row"><span class="num">6.</span><span class="line"></span></div>
        <div class="row"><span class="num">7.</span><span class="line"></span></div>
        <div class="row"><span class="num">8.</span><span class="line"></span></div>
      </div>
    </div>
  </section>

  <section class="panel homework">
    <h2 class="panel-title">HOMEWORK</h2>
    <div class="row"><span class="label">Subject</span><span class="line"></span></div>
    <div class="row"><span class="label">Task</span><span class="line"></span></div>
    <div class="row"><span class="label">Subject</span><span class="line"></span></div>
    <div class="row"><span class="label">Task</span><span class="line"></span></div>
    <div class="row"><span class="label">Subject</span><span class="line"></span></div>
    <div class="row"><span class="label">Task</span><span class="line"></span></div>
    <div class="row"><span class="label">Subject</span><span class="line"></span></div>
    <div class="row"><span class="label">Task</span><span class="line"></span></div>
    <div class="row"><span class="label">Subject</span><span class="line"></span></div>
    <div class="row"><span class="label">Task</span><span class="line"></span></div>
    <div class="row"><span class="label">Subject</span><span class="line"></span></div>
    <div class="row"><span class="label">Task</span><span class="line"></span></div>
  </section>

  <section class="panel assessments">
    <h2 class="panel-title">ASSESSTMENTS</h2>
    <div class="row"><span class="label">Assessment:</span><span class="line"></span><span class="due">Due</span><span class="due-line"></span></div>
    <div class="row"><span class="label">Element:</span><span class="line"></span></div>
    <div class="row"><span class="label">Assessment:</span><span class="line"></span><span class="due">Due</span><span class="due-line"></span></div>
    <div class="row"><span class="label">Element:</span><span class="line"></span></div>
    <div class="row"><span class="label">Assessment:</span><span class="line"></span><span class="due">Due</span><span class="due-line"></span></div>
    <div class="row"><span class="label">Element:</span><span class="line"></span></div>
    <div class="row"><span class="label">Assessment:</span><span class="line"></span><span class="due">Due</span><span class="due-line"></span></div>
    <div class="row"><span class="label">Element:</span><span class="line"></span></div>
    <div class="row"><span class="label">Assessment:</span><span class="line"></span><span class="due">Due</span><span class="due-line"></span></div>
    <div class="row"><span class="label">Element:</span><span class="line"></span></div>
    <div class="row"><span class="label">Assessment:</span><span class="line"></span><span class="due">Due</span><span class="due-line"></span></div>
    <div class="row"><span class="label">Element:</span><span class="line"></span></div>
  </section>

  <div class="bottom-row">
    <section class="panel notes">
      <h2 class="panel-title">NOTES</h2>
      <div class="row"><span class="line"></span></div>
      <div class="row"><span class="line"></span></div>
      <div class="row"><span class="line"></span></div>
      <div class="row"><span class="line"></span></div>
    </section>
    <section class="panel practice">
      <h2 class="panel-title">PRACTICE</h2>
      <div class="row"><span class="line"></span></div>
      <div class="row"><span class="line"></span></div>
      <div class="row"><span class="line"></span></div>
      <div class="row"><span class="line"></span></div>
    </section>
  </div>
</main>
</body>
</html>
```